Marriage Retreat: 4 Page Color Brochure

I need a 4 page, full color brochure that is 8.5 x 11 when folded (11 x 17 front/back when printed/unfolded). The brochure is to inform pastors and religious leaders about a private retreat to help them strengthen their marriages. Attached you will find: (1) a Word document with the copy/text and initial guidelines on the page layout (although some flexibility on what text goes on which page is acceptable); (2) a creative brief PDF with some of the visual ideas I have to jumpstart your thinking; (3) logo files for the organization Steadfast Vows (the logo must be included); (4) original scan of tree artwork that can be used as a visual element (this is the same tree that has been converted to a vector file in the logo; please use a color scheme in the brochure that is complementary to this artwork). The overall feel for this piece should be timeless, classic, welcoming and approachable. The font in the logo is Audrey, although it has been stylized a bit. Please take that into account when selecting fonts for the layout. I do not yet have the photo of Dale & Norma (the hosts of this retreat) for you to include with their bios. Please insert a placeholder image for now and I will get you the actual photo in a few days. Once we get to the final stage, I would also like to have a version of the file that is laid out as 4 individual 8.5x11 pages so it can be printed in that format if needed. I would also like to have a PDF version of each file.

Target Market(s)

The initial target market for this type of service will be males (who typically recommend the service to couples), but the ultimate decision maker will probably be a female (the wife of the couple that will attend the retreat).

Industry/Entity Type

Counseling

Font styles to use
Serif
Sans Serif
Other font styles liked:
• Audrey

Colors

Designer to choose colors to be used in the design.

Requirements
Must have
• Logo for Steadfast Vows. Color scheme that is complementary to the tree artwork provided. Font that incorporates or complements the font in the logo - Audrey. Photo of Dale & Norma with their bio (use a placeholder for now). Please include at least one or two stock photos of married couples somewhere in the brochure. See the examples in the creative brief and please let me know if you need me to provide the actual files (if you do not have access to Pixmeadow Library).
Nice to have
• A design option that includes an infographic/icon style for me to consider. See creative brief document for more on this idea.
Should not have
• Note: I removed the prior instructions indicating this design should not have a full page bleed. That is no longer a limitation on this design. Feel free to go with what you think looks best to make your submission as strong as possible.

```html
<!DOCTYPE html>
<html lang="en">
<head>
<meta charset="utf-8">
<title>Steadfast Vows – Retreat Brochure</title>
<link href="https://fonts.googleapis.com/css2?family=Marcellus&family=Arimo:ital,wght@0,400;0,700;1,400&display=swap" rel="stylesheet">
<style>
:root{
  --canvas:#f1f1f1;
  --green:#2f6b33;
  --green-dark:#245a28;
  --green-mid:#4d8a3c;
  --green-light:#a9cf6e;
  --lime:#d6e98f;
  --ink:#333;
  --white:#fff;
}
*{box-sizing:border-box;margin:0;padding:0}
html,body{width:1200px;height:1000px;overflow:hidden}
body{background:var(--canvas);position:relative;font-family:"Arimo",Arial,sans-serif;color:var(--ink)}
.spread{position:absolute;left:243px;width:717px;box-shadow:0 6px 10px rgba(0,0,0,.18);overflow:hidden;background:var(--white)}
.spread--outside{top:8px;height:467px}
.spread--inside{top:505px;height:465px}
.abs{position:absolute}

/* back page agenda */
.agenda{left:0;top:0;width:147px;height:467px;background:var(--white);padding:14px 4px 14px 12px}
.agenda h2{font-family:"Marcellus",Georgia,serif;color:var(--green);font-size:15px;font-weight:400;line-height:1;margin-bottom:4px}
.agenda h3{font-family:"Marcellus",Georgia,serif;color:var(--green);font-size:8.5px;font-weight:400;margin:6px 0 2px}
.agenda p{font-size:6px;line-height:1.34;white-space:nowrap}
.agenda .note{color:var(--green);font-style:italic;margin-top:7px;white-space:normal;padding-right:6px}
.brand{display:flex;align-items:center;gap:5px;color:var(--green);font-family:"Marcellus",Georgia,serif;font-weight:400}
.brand i{display:block;border-radius:50%;background:var(--green-mid)}
.agenda .brand{position:absolute;left:14px;top:395px;font-size:13px}
.agenda .brand i{width:10px;height:10px}

.contact{left:147px;top:0;width:211px;height:467px;background:linear-gradient(180deg,#5f8d4c 0%,#3d7336 45%,var(--green-dark) 100%);padding:236px 13px 0 13px;color:var(--white)}
.contact-photo{position:absolute;left:0;top:0;width:211px;height:235px;background:radial-gradient(ellipse at 45% 40%,#8aa870 0%,#5f8a4c 55%,rgba(61,115,54,0) 100%)}
.contact h2{position:relative;font-family:"Marcellus",Georgia,serif;font-weight:400;color:var(--lime);font-size:12.5px;line-height:1.3;margin-bottom:6px}
.contact p{position:relative;font-size:9.3px;line-height:1.25;margin-bottom:9px}
.contact .email{font-weight:700}
.contact small{position:relative;display:block;font-size:5px;line-height:1.4;margin-bottom:5px}

.spine{left:358px;top:0;width:67px;height:467px;background:var(--green)}
.cover{left:425px;top:0;width:292px;height:467px;background:linear-gradient(160deg,#f3ece4 0%,#ead7c4 45%,#d9b595 70%,#c9a27e 100%)}
.cover-photo{position:absolute;left:0;top:150px;width:292px;height:230px;background:radial-gradient(ellipse at 55% 45%,#efc6a6 0%,#e2b08b 45%,rgba(234,215,196,0) 80%)}
.cover .brand{position:absolute;left:0;right:0;top:80px;justify-content:center;font-size:17px}
.cover .brand i{width:12px;height:12px}
.cover h1{position:absolute;right:14px;top:388px;text-align:right;font-family:"Marcellus",Georgia,serif;font-weight:400;color:var(--green);font-size:19px;line-height:1.12}

/* inside */
.topline{left:0;top:0;width:717px;height:6px;background:var(--green)}
.page-left{left:0;top:6px;width:358px;height:329px;background:linear-gradient(90deg,#fff 0%,#fff 75%,#eeeeec 100%)}
.page-right{left:358px;top:6px;width:359px;height:329px;background:var(--white)}
.page-left h2,.page-right h2{font-family:"Marcellus",Georgia,serif;font-weight:400;color:var(--green);font-size:14px;line-height:1}
.stat{position:absolute;width:110px;text-align:center;font-size:8px;line-height:1.2}
.stat svg{display:block;margin:0 auto}
.invite p{font-size:8.3px;line-height:1.28}
.pill{position:absolute;top:257px;width:104px;height:60px;border:1.5px solid var(--green);border-radius:4px;overflow:hidden;text-align:center}
.pill b{display:flex;align-items:center;justify-content:center;height:18px;font-family:"Marcellus",Georgia,serif;font-weight:400;color:var(--green);font-size:8px;line-height:1;background:var(--white)}
.pill span{display:flex;align-items:center;justify-content:center;height:41px;background:linear-gradient(180deg,#5a9a45,var(--green));color:var(--white);font-size:8px;line-height:1.2;padding:0 8px}
.plus{position:absolute;top:279px;z-index:2;font-size:13px;color:var(--ink);font-weight:700;width:12px;text-align:center}
.page-right p{font-size:8px;line-height:1.3}
.photo-couple{position:absolute;left:188px;top:37px;width:155px;height:106px;background:linear-gradient(135deg,#e7e4de 0%,#c9c1b5 50%,#6b5a4c 100%)}
.photo-hosts{position:absolute;left:22px;top:150px;width:150px;height:179px;background:linear-gradient(180deg,#fff 0%,#d6d3d0 18%,#7a7674 45%,#45454a 75%,#5b6470 100%);border-radius:40px 40px 0 0}

.testimonials{left:0;top:335px;width:717px;height:130px;background:var(--green);color:var(--white);padding:6px 16px 0}
.testimonials h2{font-family:"Marcellus",Georgia,serif;font-weight:400;color:var(--lime);text-align:center;font-size:14px;line-height:1;margin-bottom:6px}
.quotes{display:grid;grid-template-columns:repeat(4,1fr);gap:14px}
.quotes blockquote{font-style:italic;font-size:6.3px;line-height:1.3;margin-bottom:6px;position:relative;padding:0 6px 0 8px;text-align:justify}
.quotes blockquote::before{content:"\201C";position:absolute;left:-1px;top:-3px;font-size:12px;font-style:normal}
.quotes blockquote::after{content:"\201D";position:absolute;right:-2px;bottom:-7px;font-size:12px;font-style:normal}
</style>
</head>
<body>

<section class="spread spread--outside">
  <div class="abs agenda">
    <h2>SAMPLE AGENDA</h2>
    <h3>DAY ONE</h3>
    <p>Arrive, settle in, get acquainted<br>Individual reflection and couple connection<br>Lunch<br>Session 1*<br>Break<br>Session 2<br>Free time<br>Dinner<br>5 minute huddle</p>
    <h3>DAY TWO</h3>
    <p>Coffee, individual reflection, time with God<br>Breakfast<br>Couple breakout<br>Session 3<br>Break<br>Session 4: Building Bridges part 1<br>Break<br>Session 5: Building Bridges part 2<br>Free time<br>Dinner date (couple only)<br>5 minute huddle</p>
    <h3>DAY THREE</h3>
    <p>Coffee, individual reflection and time with God<br>Breakfast<br>Session 6: Integrated Intimacy<br>Lunch<br>Break<br>Session 7<br>Wrap up, next steps<br>Pray<br>Depart</p>
    <p class="note">* Each session lasts approximately 2 hours and includes time with the hosts and breakouts for reflection and exercises.</p>
    <div class="brand"><i></i>Steadfast Vows</div>
  </div>

  <div class="abs contact">
    <div class="contact-photo" role="img" aria-label="Smiling married couple, tinted green"></div>
    <h2>READY TO INVEST IN<br>YOUR MARRIAGE?</h2>
    <p>Contact Dale &amp; Norma Hollis to request a confidential initial consultation:<br><span class="email">info@steadfastvowsretreat.com</span></p>
    <p>Retreat expenses are covered for you including meals, lodging, teaching and materials. Couples are responsible for their own transportation to the retreat and childcare, if needed. Additional scholarships are available.</p>
    <small>¹ The Ardent Institute, 2006<br>² Kestrel Research Group, Shepherds Under Strain, 2017</small>
    <small>Testimonials have been edited for clarity and confidentiality.</small>
    <small>© Dale and Norma Hollis. Tree artwork by Lena Marsh.<br>Photo of Hollises by Brookline Studio</small>
  </div>

  <div class="abs spine"></div>

  <div class="abs cover">
    <div class="cover-photo" role="img" aria-label="Close-up of a couple holding hands"></div>
    <div class="brand"><i></i>Steadfast Vows</div>
    <h1>A Personalized<br>RETREAT FOR<br>COUPLES IN MINISTRY</h1>
  </div>
</section>

<section class="spread spread--inside">
  <div class="abs topline"></div>

  <div class="abs page-left">
    <h2 class="abs" style="left:17px;top:16px">MINISTRY MARRIAGES ARE AT RISK</h2>

    <div class="stat" style="left:14px;top:48px">
      <svg width="80" height="100" viewBox="0 0 80 100" aria-hidden="true">
        <circle cx="40" cy="40" r="37" fill="none" stroke="#dbeaa9" stroke-width="4"/>
        <circle cx="40" cy="40" r="37" fill="none" stroke="var(--green-light)" stroke-width="4" stroke-dasharray="179 233" transform="rotate(-90 40 40)"/>
        <circle cx="40" cy="40" r="29" fill="var(--green-mid)"/>
        <text x="40" y="46" text-anchor="middle" fill="#fff" font-family="Arimo,Arial,sans-serif" font-weight="700" font-size="16">77%</text>
        <line x1="40" y1="80" x2="40" y2="94" stroke="var(--green)" stroke-dasharray="2 2"/>
        <path d="M36 93 L40 99 L44 93" fill="none" stroke="var(--green)"/>
      </svg>
      of pastors feel<br>they do not have<br>a good marriage¹
    </div>
    <div class="stat" style="left:125px;top:48px">
      <svg width="80" height="100" viewBox="0 0 80 100" aria-hidden="true">
        <circle cx="40" cy="40" r="37" fill="none" stroke="#dbeaa9" stroke-width="4"/>
        <circle cx="40" cy="40" r="37" fill="none" stroke="var(--green-light)" stroke-width="4" stroke-dasharray="112 233" transform="rotate(-90 40 40)"/>
        <circle cx="40" cy="40" r="29" fill="var(--green-mid)"/>
        <text x="40" y="46" text-anchor="middle" fill="#fff" font-family="Arimo,Arial,sans-serif" font-weight="700" font-size="16">48%</text>
        <line x1="40" y1="80" x2="40" y2="94" stroke="var(--green)" stroke-dasharray="2 2"/>
        <path d="M36 93 L40 99 L44 93" fill="none" stroke="var(--green)"/>
      </svg>
      say their current ministry<br>role has been difficult<br>on their marriage²
    </div>
    <div class="stat" style="left:240px;top:48px">
      <svg width="80" height="100" viewBox="0 0 80 100" aria-hidden="true">
        <circle cx="40" cy="40" r="37" fill="none" stroke="#dbeaa9" stroke-width="4"/>
        <circle cx="40" cy="40" r="37" fill="none" stroke="var(--green-light)" stroke-width="4" stroke-dasharray="61 233" transform="rotate(-90 40 40)"/>
        <circle cx="40" cy="40" r="29" fill="var(--green-mid)"/>
        <text x="40" y="46" text-anchor="middle" fill="#fff" font-family="Arimo,Arial,sans-serif" font-weight="700" font-size="16">26%</text>
        <line x1="40" y1="80" x2="40" y2="94" stroke="var(--green)" stroke-dasharray="2 2"/>
        <path d="M36 93 L40 99 L44 93" fill="none" stroke="var(--green)"/>
      </svg>
      of pastors<br>face significant<br>marital problems³
    </div>

    <div class="abs invite" style="left:17px;top:196px;width:320px">
      <h2 style="margin-bottom:9px">YOUR INVITATION</h2>
      <p>Whether your marriage is thriving, in distress, or needs a fresh start, Steadfast Vows retreats equip couples in ministry to:</p>
    </div>

    <div class="pill" style="left:17px"><b>DEEPEN INTIMACY</b><span>Reinvigorate love by being heard and valued</span></div>
    <div class="plus" style="left:121px">+</div>
    <div class="pill" style="left:133px"><b>UNTANGLE<br>RELATIONAL KNOTS</b><span>Heal hurts, care for yourself and each other with grace</span></div>
    <div class="plus" style="left:237px">+</div>
    <div class="pill" style="left:249px"><b>REPLENISH JOY</b><span>Create an environment to grow and rediscover fun</span></div>
  </div>

  <div class="abs page-right">
    <h2 class="abs" style="left:24px;top:13px">A RETREAT FOR COUPLES IN MINISTRY</h2>
    <div class="abs" style="left:24px;top:38px;width:156px">
      <p style="margin-bottom:6px">Steadfast Vows retreats provide you time, space, and Bible-based tools to cultivate a life-giving marriage.</p>
      <p>The 3-day retreat is personally tailored for one couple only. We provide a lovely, comfortable, private and safe setting where everything is taken care of. We can welcome you to our locations in Austin and Chicago or in special circumstances bring the retreat to your area.</p>
    </div>
    <div class="photo-couple" role="img" aria-label="Couple sitting together in conversation"></div>
    <div class="photo-hosts" role="img" aria-label="Portrait of hosts Dale and Norma Hollis"></div>
    <h2 class="abs" style="left:186px;top:164px">YOUR HOSTS</h2>
    <p class="abs" style="left:186px;top:186px;width:160px">Dale and Norma Hollis bring more than 20 years of experience helping build and restore Christ-centered marriages. They have experienced God's redemption in their own broken stories. A compassionate and insightful listener, Dale is a retired energy industry leader currently serving on a corporate board and church overseer board. Norma formerly served in full-time ministry and is a gifted teacher who delights in unpacking God's truth. God has used the time and tools they offer to transform many marriages.</p>
  </div>

  <div class="abs testimonials">
    <h2>EXPERIENCE TRANSFORMATION</h2>
    <div class="quotes">
      <div>
        <blockquote>Our marriage was in crisis. The stress of ministry had taken a deep toll on us and in the worst moments we didn't even like each other anymore. Dale and Norma are people we trust with the darkest moments of our lives. They stood with us and held up our arms to allow us to continue.</blockquote>
        <blockquote>During a critical time, Dale and Norma helped us navigate our marriage around the traps that we so easily and repeatedly fell into… We were sitting ducks for the evil one… They took us to the deep end of the marriage pool and dove in first. I see a more fruitful and God honoring marriage ahead.</blockquote>
      </div>
      <div>
        <blockquote>This experience was the most important thing I have ever done in my life outside of saying yes to Jesus. As a pastor, I have always known that my family is my number one ministry. This experience helped me take that theoretical goal and turn it into a reality.</blockquote>
        <blockquote>Dale and Norma meet people in their pain and brokenness without shame or judgment and gently help them make major shifts from a place of extreme distress to a hopeful and productive path forward.</blockquote>
      </div>
      <div>
        <blockquote>Dale and Norma understand the sanctity of safely and compassionately learning from each other's stories…the triumphs, the failures, the times of healing, and the times of deep woundedness. They hold the stories of the couples they work tenderly, confidentially and dearly.</blockquote>
        <blockquote>Dale and Norma exemplify these qualities: a safety zone with in-the-vault assurance, advice grounded in scripture, a straightforward message, truth spoken in love even when painful, vulnerability and authenticity.</blockquote>
      </div>
      <div>
        <blockquote>Dale and Norma are tender-hearted, caring, full of compassion, and willing to press into the real issues to help bring needed healing and health to couples they work with… They understand the hard work it will take to get healthy and are willing to fight alongside couples to help them wrestle with the hardships they might have encountered in life and marriage… Dale and Norma are gifted with discernment and will help you navigate the wounds that are recognized and the wounds that still need to be discovered.</blockquote>
      </div>
    </div>
  </div>
</section>

</body>
</html>
```